Helping Seniors and their families start the discussion about driver safety, and explore options to preserve senior independence.
Target Market(s)
Seniors and their families
Industry/Entity Type
Non Profit
Number of Pages Required
4 page
Font styles to use
Sans Serif
Requirements
Must have
- Logo
- Application for Bright Pathways Registration

Nice to have
- Colorful, and designed for Senior Citizens and their Families

```html
<!DOCTYPE html>
<html lang="en">
<head>
<meta charset="utf-8">
<title>Bright Pathways</title>
<link href="https://fonts.googleapis.com/css2?family=Roboto+Condensed:wght@400;700&family=Open+Sans:ital,wght@0,400;0,600;1,400&display=swap" rel="stylesheet">
<style>
:root{
  --green:#0b8a4b;
  --green-dark:#08723d;
  --ink:#333333;
  --muted:#6f6f6f;
  --light:#f4f4f4;
  --line:#d9d9d9;
  --footer:#1e1e1e;
  --white:#ffffff;
}
*{margin:0;padding:0;box-sizing:border-box}
html,body{width:1200px;height:2922px;overflow:hidden}
body{position:relative;background:var(--white);font-family:"Open Sans",Arial,sans-serif;color:var(--ink)}
.abs{position:absolute}
.head{font-family:"Roboto Condensed",Arial,sans-serif}

/* header */
.site-header{top:0;left:0;width:1200px;height:125px;background:var(--white)}
.brand{left:97px;top:20px;display:flex;align-items:center;gap:10px}
.brand-name{font-family:"Roboto Condensed",Arial,sans-serif;font-weight:700;font-size:36px;line-height:33px;color:var(--green)}
.brand-dot{width:40px;height:40px;border-radius:50%;background:var(--ink)}
.header-phone{left:818px;top:28px;font-family:"Roboto Condensed",sans-serif;font-size:19px;color:#222;display:flex;align-items:center;gap:6px}
.book-btn{left:973px;top:23px;width:128px;height:35px;border-radius:18px;background:var(--green);color:var(--white);font-family:"Roboto Condensed",sans-serif;font-weight:700;font-size:13px;display:flex;align-items:center;justify-content:center}
.main-nav{top:82px;left:0;width:1200px;height:43px;font-family:"Roboto Condensed",sans-serif;font-size:13px;color:#444;letter-spacing:.3px}
.main-nav span{position:absolute;top:0}
.main-nav .active{color:var(--green)}
.main-nav .active::after{content:"";position:absolute;left:-6px;right:-6px;top:38px;height:3px;background:var(--green)}

/* hero */
.hero{top:125px;left:0;width:1200px;height:520px;background:linear-gradient(100deg,#4a4f48 0%,#6d7469 30%,#9ba294 55%,#6f7a6a 78%,#3c4a38 100%)}
.hero-title{left:97px;top:292px;font-family:"Roboto Condensed",sans-serif;font-size:48px;color:var(--white);letter-spacing:.5px}
.hero-sub{left:97px;top:357px;font-size:17px;line-height:25px;color:var(--white)}
.hero-btn{left:97px;top:422px;width:176px;height:40px;background:var(--green);color:var(--white);font-family:"Roboto Condensed",sans-serif;font-weight:700;font-size:14px;display:flex;align-items:center;justify-content:center}
.hero-arrow{top:372px}

/* welcome */
.welcome{top:645px;left:0;width:1200px;height:230px;background:var(--light)}
.section-title{font-family:"Roboto Condensed",sans-serif;font-size:29px;color:#2b2b2b;text-align:center;width:1200px;left:0}
.rule{height:2px;background:#444;width:70px}
.welcome-text{left:135px;top:758px;width:930px;text-align:center;font-size:11.5px;line-height:21px;color:var(--muted)}

/* why */
.feature{width:300px}
.feature-icon{position:absolute;left:0;top:0;width:54px;height:54px;border-radius:50%;background:var(--green);display:flex;align-items:center;justify-content:center}
.feature-title{position:absolute;left:69px;top:-2px;font-family:"Roboto Condensed",sans-serif;font-size:18px;color:#333;white-space:nowrap}
.feature-text{position:absolute;left:69px;top:28px;width:230px;font-size:11.5px;line-height:21px;color:var(--muted)}

/* reservation */
.res-band{top:1380px;left:0}
.res-title{top:1462px;font-family:"Roboto Condensed",sans-serif;font-size:29px;color:var(--white);text-align:center;width:1200px;left:0}
.step-text{width:240px;text-align:center;font-family:"Roboto Condensed",sans-serif;font-size:15px;line-height:23px;color:var(--white)}
.res-note{top:1780px;left:0;width:1200px;text-align:center;font-family:"Roboto Condensed",sans-serif;font-size:17px;line-height:25px;color:var(--white)}

/* services */
.services-photo{left:97px;top:1964px;width:444px;height:282px;border:4px solid #eaeaea;box-shadow:0 0 0 1px #d5d5d5;background:linear-gradient(120deg,#8a5a48 0%,#b07b62 35%,#c8c6c0 60%,#7f8c84 100%)}
.services-title{left:577px;top:1966px;font-family:"Roboto Condensed",sans-serif;font-size:29px;color:#2b2b2b}
.services-intro{left:577px;top:2010px;width:530px;font-size:11.5px;line-height:20px;color:#555}
.service-list{list-style:none;font-size:11.5px;line-height:23px;color:#444}
.service-list li{display:flex;align-items:center;gap:9px}
.chev{width:11px;height:11px;flex:none}

/* testimonial */
.testimonial{top:2345px;left:0;width:1200px;height:215px;background:#f5f5f5}
.partner-badge{left:97px;top:2412px;width:120px;height:50px;border-radius:4px;background:#ffffff;border:2px solid #2b2b2b}
.quote{left:318px;top:2393px;width:790px;font-style:italic;font-size:11.5px;line-height:21px;color:#555}
.quote-by{left:318px;top:2492px;font-style:italic;font-size:12px;color:#555}

/* footer */
.site-footer{top:2560px;left:0;width:1200px;height:362px;background:var(--footer)}
.foot-brand{left:97px;top:2600px;display:flex;align-items:center;gap:10px}
.foot-brand .brand-name{color:var(--white);font-size:32px;line-height:29px}
.foot-brand .brand-dot{background:var(--white);width:34px;height:34px}
.foot-contact{left:97px;font-size:12.5px;line-height:19px;color:#e6e6e6;display:flex;gap:14px;align-items:flex-start}
.foot-heading{font-family:"Roboto Condensed",sans-serif;font-size:16px;color:var(--white);letter-spacing:.3px}
.foot-text{left:418px;top:2648px;width:300px;font-size:11.5px;line-height:20px;color:#e6e6e6}
.foot-input{left:418px;top:2702px;width:286px;height:40px;background:var(--white);font-size:11.5px;color:#666;padding:12px 10px}
.foot-btn{left:418px;top:2755px;width:98px;height:38px;background:var(--green);color:var(--white);font-family:"Roboto Condensed",sans-serif;font-weight:700;font-size:12px;display:flex;align-items:center;justify-content:center}
.quick-links{left:800px;top:2646px;list-style:none;font-size:12.5px;line-height:24px;color:#e6e6e6}
.social{left:1000px;top:2645px;list-style:none;font-size:14px;color:#e6e6e6}
.social li{display:flex;align-items:center;gap:9px;height:37px}
.social .ring{width:26px;height:26px;border:1.5px solid #e6e6e6;border-radius:50%}
.foot-rule{left:0;top:2858px;width:1200px;height:1px;background:#333}
.copyright{left:0;top:2884px;width:1200px;text-align:center;font-size:12px;color:#e6e6e6}
</style>
</head>
<body>

<header class="site-header abs">
  <div class="brand abs">
    <div class="brand-name">Bright<br>Pathways</div>
    <div class="brand-dot"></div>
  </div>
  <div class="header-phone abs">
    <svg width="15" height="15" viewBox="0 0 24 24"><path fill="#222" d="M6.6 10.8a15.2 15.2 0 0 0 6.6 6.6l2.2-2.2c.3-.3.7-.4 1-.2 1.1.4 2.3.6 3.6.6.6 0 1 .4 1 1V20c0 .6-.4 1-1 1A17 17 0 0 1 3 4c0-.6.4-1 1-1h3.5c.6 0 1 .4 1 1 0 1.3.2 2.5.6 3.6.1.3 0 .7-.2 1z"/></svg>
    <span>+555-014-2730</span>
  </div>
  <div class="book-btn abs">BOOKING NOW!</div>
  <nav class="main-nav abs">
    <span class="active" style="left:494px">HOME</span>
    <span style="left:565px">ABOUT US</span>
    <span style="left:661px">WHY BRIGHT PATHWAYS?</span>
    <span style="left:836px">RESERVATION</span>
    <span style="left:955px">BLOG</span>
    <span style="left:1021px">CONTACT US</span>
  </nav>
</header>

<section class="hero abs" role="img" aria-label="Photo of a smiling caregiver helping an older man step out of a car"></section>
<div class="hero-title abs">BRIGHT PATHWAYS</div>
<div class="hero-sub abs">Premier Transportation for Seniors<br>and Disabled Persons</div>
<div class="hero-btn abs">MAKE A RESERVATION</div>
<svg class="hero-arrow abs" style="left:38px" width="14" height="20" viewBox="0 0 14 20"><path d="M11 2 3 10l8 8" fill="none" stroke="#fff" stroke-width="2.5"/></svg>
<svg class="hero-arrow abs" style="left:1150px" width="14" height="20" viewBox="0 0 14 20"><path d="m3 2 8 8-8 8" fill="none" stroke="#fff" stroke-width="2.5"/></svg>

<section class="welcome abs"></section>
<h2 class="section-title abs" style="top:706px">WELCOME TO BRIGHT PATHWAYS</h2>
<div class="rule abs" style="left:300px;top:726px"></div>
<div class="rule abs" style="left:830px;top:726px"></div>
<p class="welcome-text abs">Bright Pathways helps seniors and their families talk openly about driver safety and plan trusted rides that keep daily life moving. Our caring drivers offer door-to-door help, patient assistance and a friendly face for every trip, so independence never has to end when the car keys are set aside. We serve neighbours across the metro area every day of the week.</p>

<h2 class="section-title abs" style="top:948px">WHY BRIGHT PATHWAYS?</h2>

<div class="feature abs" style="left:97px;top:1060px">
  <div class="feature-icon"><svg width="26" height="26" viewBox="0 0 24 24"><path fill="#fff" d="M11 3a9 9 0 1 0 9 10h-9z"/><path fill="#fff" d="M13 1v10h10A10 10 0 0 0 13 1z"/></svg></div>
  <div class="feature-title">Convenience</div>
  <div class="feature-text">With Bright Pathways, you can schedule transportation at a time that is convenient for you, eliminating the need to work</div>
</div>
<div class="feature abs" style="left:456px;top:1060px">
  <div class="feature-icon"><svg width="26" height="26" viewBox="0 0 24 24"><path fill="#fff" d="M5 11 7 5h10l2 6h1v7h-2v2h-3v-2H9v2H6v-2H4v-7zm2.5 0h9l-1.2-4H8.7zM7 15.5a1.5 1.5 0 1 0 0-.1zm10 0a1.5 1.5 0 1 0 0-.1z"/></svg></div>
  <div class="feature-title">Specialized Services</div>
  <div class="feature-text">Our team is experienced in providing services to seniors and individuals with physical and cognitive issues such as blindness.</div>
</div>
<div class="feature abs" style="left:810px;top:1060px">
  <div class="feature-icon"><svg width="26" height="26" viewBox="0 0 24 24"><path fill="#fff" d="M12 2 23 21H1z"/><path fill="#0b8a4b" d="M11 9h2v6h-2zm0 7.5h2v2h-2z"/></svg></div>
  <div class="feature-title">Safety</div>
  <div class="feature-text">Your safety is our first priority. We follow you from location to location, and then follow up with you to see how</div>
</div>
<div class="feature abs" style="left:97px;top:1205px">
  <div class="feature-icon"><svg width="24" height="24" viewBox="0 0 24 24"><path fill="#fff" d="M4 8h4a2.5 2.5 0 1 1 5 0h4v4a2.5 2.5 0 1 1 0 5v4H4v-4a2.5 2.5 0 1 0 0-5z"/></svg></div>
  <div class="feature-title">Understanding</div>
  <div class="feature-text">Your Needs We understand that everyone is not alike, therefore, needs are not alike. It is important to us that our services</div>
</div>
<div class="feature abs" style="left:456px;top:1205px">
  <div class="feature-icon"><svg width="24" height="24" viewBox="0 0 24 24"><rect x="3" y="5" width="18" height="16" fill="none" stroke="#fff" stroke-width="2"/><path d="M3 9h18M8 2v5M16 2v5M7 13h2M11 13h2M15 13h2M7 17h2M11 17h2M15 17h2" stroke="#fff" stroke-width="2"/></svg></div>
  <div class="feature-title">Evening and Weekend</div>
  <div class="feature-text">Evening and Weekend Service Life does not stop at 6 pm each weekday. We encourage our clients to remain socially active.</div>
</div>
<div class="feature abs" style="left:810px;top:1205px">
  <div class="feature-icon"><svg width="24" height="24" viewBox="0 0 24 24"><path fill="#fff" d="M3 3h9l9 9-9 9-9-9z"/><circle cx="7.5" cy="7.5" r="1.8" fill="#0b8a4b"/></svg></div>
  <div class="feature-title">Affordable Rates</div>
  <div class="feature-text">Our rate are less than rates of most taxi and transportation companies in the Metro Atlanta Area and beyond.</div>
</div>

<svg class="res-band abs" width="1200" height="490" viewBox="0 0 1200 490">
  <defs>
    <linearGradient id="resFill" x1="0" y1="0" x2="1" y2="0">
      <stop offset="0" stop-color="#0a8448"/>
      <stop offset=".5" stop-color="#0c8f4e"/>
      <stop offset="1" stop-color="#0a8347"/>
    </linearGradient>
  </defs>
  <polygon points="0,75 600,0 1200,75" fill="#f2f2f2"/>
  <polyline points="0,68 600,-4 1200,68" fill="none" stroke="#c8c8c8" stroke-width="5"/>
  <polygon points="0,75 600,5 1200,75 1200,488 0,488" fill="url(#resFill)" role="img" aria-label="Green tinted photo of a driver assisting a passenger"/>
</svg>
<h2 class="res-title abs">RESERVATION PROCESS</h2>

<svg class="abs" style="left:240px;top:1548px" width="110" height="120" viewBox="0 0 110 120">
  <path d="M55 3a52 52 0 0 1 14 102l-14 13-14-13A52 52 0 0 1 55 3z" fill="none" stroke="#fff" stroke-width="2.5"/>
  <circle cx="55" cy="55" r="18" fill="none" stroke="#fff" stroke-width="3"/>
  <path d="M55 44v12h8" fill="none" stroke="#fff" stroke-width="3"/>
</svg>
<svg class="abs" style="left:550px;top:1548px" width="110" height="120" viewBox="0 0 110 120">
  <path d="M55 3a52 52 0 0 1 14 102l-14 13-14-13A52 52 0 0 1 55 3z" fill="none" stroke="#fff" stroke-width="2.5"/>
  <rect x="37" y="40" width="36" height="32" fill="none" stroke="#fff" stroke-width="3"/>
  <path d="M37 49h36M45 34v9M65 34v9M43 56h5M53 56h5M63 56h5M43 64h5M53 64h5M63 64h5" stroke="#fff" stroke-width="3"/>
</svg>
<svg class="abs" style="left:860px;top:1548px" width="110" height="120" viewBox="0 0 110 120">
  <path d="M55 3a52 52 0 0 1 14 102l-14 13-14-13A52 52 0 0 1 55 3z" fill="none" stroke="#fff" stroke-width="2.5"/>
  <path transform="translate(38 38) scale(1.4)" fill="#fff" d="M6.6 10.8a15.2 15.2 0 0 0 6.6 6.6l2.2-2.2c.3-.3.7-.4 1-.2 1.1.4 2.3.6 3.6.6.6 0 1 .4 1 1V20c0 .6-.4 1-1 1A17 17 0 0 1 3 4c0-.6.4-1 1-1h3.5c.6 0 1 .4 1 1 0 1.3.2 2.5.6 3.6.1.3 0 .7-.2 1z"/>
</svg>
<svg class="abs" style="left:415px;top:1598px" width="80" height="20" viewBox="0 0 80 20">
  <path d="M2 15q35-12 70-6" fill="none" stroke="#fff" stroke-width="2" stroke-dasharray="5 4"/>
  <path d="M66 4l8 5-9 4" fill="none" stroke="#fff" stroke-width="2"/>
</svg>
<svg class="abs" style="left:748px;top:1618px" width="80" height="20" viewBox="0 0 80 20">
  <path d="M2 15q35-12 70-6" fill="none" stroke="#fff" stroke-width="2" stroke-dasharray="5 4"/>
  <path d="M66 4l8 5-9 4" fill="none" stroke="#fff" stroke-width="2"/>
</svg>
<p class="step-text abs" style="left:175px;top:1684px">We ask for 24 hours notice for<br>each reservation.</p>
<p class="step-text abs" style="left:485px;top:1684px">Reservations can be made 7 days<br>a week between the hours of 9<br>am and 5 pm</p>
<p class="step-text abs" style="left:795px;top:1684px">RESERVATION LINE:<br>555-019-6284</p>
<p class="res-note abs">Please leave a message with your name and phone number<br>if no one answers immediately</p>

<div class="services-photo abs" role="img" aria-label="Photo of a caregiver walking an elderly woman to a parked car"></div>
<h2 class="services-title abs">OUR SERVICES</h2>
<p class="services-intro abs">We plan each ride around your needs, from routine checkups to family visits, with drivers trained to help at every step.</p>
<ul class="service-list abs" style="left:577px;top:2062px">
  <li><svg class="chev" viewBox="0 0 12 12"><circle cx="6" cy="6" r="6" fill="#0b8a4b"/><path d="m5 3.5 2.5 2.5L5 8.5" fill="none" stroke="#fff" stroke-width="1.5"/></svg>Medical Appointment</li>
  <li><svg class="chev" viewBox="0 0 12 12"><circle cx="6" cy="6" r="6" fill="#0b8a4b"/><path d="m5 3.5 2.5 2.5L5 8.5" fill="none" stroke="#fff" stroke-width="1.5"/></svg>Dental Appointments</li>
  <li><svg class="chev" viewBox="0 0 12 12"><circle cx="6" cy="6" r="6" fill="#0b8a4b"/><path d="m5 3.5 2.5 2.5L5 8.5" fill="none" stroke="#fff" stroke-width="1.5"/></svg>Outpatient Testing and Procedures</li>
  <li><svg class="chev" viewBox="0 0 12 12"><circle cx="6" cy="6" r="6" fill="#0b8a4b"/><path d="m5 3.5 2.5 2.5L5 8.5" fill="none" stroke="#fff" stroke-width="1.5"/></svg>Physical Therapy</li>
  <li><svg class="chev" viewBox="0 0 12 12"><circle cx="6" cy="6" r="6" fill="#0b8a4b"/><path d="m5 3.5 2.5 2.5L5 8.5" fill="none" stroke="#fff" stroke-width="1.5"/></svg>Dialysis Clinic</li>
  <li><svg class="chev" viewBox="0 0 12 12"><circle cx="6" cy="6" r="6" fill="#0b8a4b"/><path d="m5 3.5 2.5 2.5L5 8.5" fill="none" stroke="#fff" stroke-width="1.5"/></svg>Radiation Clinics</li>
  <li><svg class="chev" viewBox="0 0 12 12"><circle cx="6" cy="6" r="6" fill="#0b8a4b"/><path d="m5 3.5 2.5 2.5L5 8.5" fill="none" stroke="#fff" stroke-width="1.5"/></svg>Church Events</li>
  <li><svg class="chev" viewBox="0 0 12 12"><circle cx="6" cy="6" r="6" fill="#0b8a4b"/><path d="m5 3.5 2.5 2.5L5 8.5" fill="none" stroke="#fff" stroke-width="1.5"/></svg>Senior Centers/Adult Care Centers</li>
</ul>
<ul class="service-list abs" style="left:840px;top:2062px">
  <li><svg class="chev" viewBox="0 0 12 12"><circle cx="6" cy="6" r="6" fill="#0b8a4b"/><path d="m5 3.5 2.5 2.5L5 8.5" fill="none" stroke="#fff" stroke-width="1.5"/></svg>Hospital/Nursing Home Discharge</li>
  <li><svg class="chev" viewBox="0 0 12 12"><circle cx="6" cy="6" r="6" fill="#0b8a4b"/><path d="m5 3.5 2.5 2.5L5 8.5" fill="none" stroke="#fff" stroke-width="1.5"/></svg>Airport Transportation</li>
  <li><svg class="chev" viewBox="0 0 12 12"><circle cx="6" cy="6" r="6" fill="#0b8a4b"/><path d="m5 3.5 2.5 2.5L5 8.5" fill="none" stroke="#fff" stroke-width="1.5"/></svg>Special Family Events</li>
  <li><svg class="chev" viewBox="0 0 12 12"><circle cx="6" cy="6" r="6" fill="#0b8a4b"/><path d="m5 3.5 2.5 2.5L5 8.5" fill="none" stroke="#fff" stroke-width="1.5"/></svg>Grocery Shopping and other Types of shopping</li>
  <li><svg class="chev" viewBox="0 0 12 12"><circle cx="6" cy="6" r="6" fill="#0b8a4b"/><path d="m5 3.5 2.5 2.5L5 8.5" fill="none" stroke="#fff" stroke-width="1.5"/></svg>Bank and Post Office Errands</li>
  <li><svg class="chev" viewBox="0 0 12 12"><circle cx="6" cy="6" r="6" fill="#0b8a4b"/><path d="m5 3.5 2.5 2.5L5 8.5" fill="none" stroke="#fff" stroke-width="1.5"/></svg>Barber/Beauty Shop Appointments</li>
</ul>

<section class="testimonial abs"></section>
<div class="partner-badge abs"></div>
<p class="quote abs">“ My mother was nervous about giving up her car, but Bright Pathways made the change easy. The drivers are kind and on time, and they wait with her at every appointment. She still runs her own errands and sees her friends each week, and our whole family feels calmer knowing she is in safe hands on every ride.</p>
<div class="quote-by abs">Marion Hale — Bright Pathways</div>
<svg class="abs" style="left:536px;top:2496px" width="36" height="12" viewBox="0 0 36 12"><path d="M7 2 3 6l4 4M3 6h7M29 2l4 4-4 4M33 6h-7" fill="none" stroke="#444" stroke-width="1.4"/></svg>

<footer class="site-footer abs"></footer>
<div class="foot-brand abs">
  <div class="brand-name">Bright<br>Pathways</div>
  <div class="brand-dot"></div>
</div>
<div class="foot-contact abs" style="top:2693px">
  <svg width="14" height="20" viewBox="0 0 14 20"><path d="M7 1a6 6 0 0 0-6 6c0 4.5 6 12 6 12s6-7.5 6-12a6 6 0 0 0-6-6z" fill="none" stroke="#e6e6e6" stroke-width="1.5"/><circle cx="7" cy="7" r="2" fill="none" stroke="#e6e6e6" stroke-width="1.5"/></svg>
  <span>Bright Pathways 48 Maple Grove<br>Lane Springfield 20417</span>
</div>
<div class="foot-contact abs" style="top:2743px">
  <svg width="16" height="16" viewBox="0 0 24 24"><path fill="none" stroke="#e6e6e6" stroke-width="1.8" d="M6.6 10.8a15.2 15.2 0 0 0 6.6 6.6l2.2-2.2c.3-.3.7-.4 1-.2 1.1.4 2.3.6 3.6.6.6 0 1 .4 1 1V20c0 .6-.4 1-1 1A17 17 0 0 1 3 4c0-.6.4-1 1-1h3.5c.6 0 1 .4 1 1 0 1.3.2 2.5.6 3.6.1.3 0 .7-.2 1z"/></svg>
  <span>Phone : 555-014-2730</span>
</div>
<div class="foot-contact abs" style="top:2776px">
  <svg width="17" height="13" viewBox="0 0 17 13"><rect x=".75" y=".75" width="15.5" height="11.5" fill="none" stroke="#e6e6e6" stroke-width="1.5"/><path d="m1 1 7.5 6L16 1" fill="none" stroke="#e6e6e6" stroke-width="1.5"/></svg>
  <span>E-mail: info@brightpathways.org</span>
</div>

<div class="foot-heading abs" style="left:418px;top:2612px">SIGN UP TO RECEIVE EMAIL</div>
<p class="foot-text abs">News, tips and ride updates for families, sent once a month.</p>
<div class="foot-input abs">Enter Name</div>
<div class="foot-btn abs">SUBSCRIBE</div>

<div class="foot-heading abs" style="left:800px;top:2612px">QUICK LINKS</div>
<ul class="quick-links abs">
  <li>Home</li><li>About Us</li><li>Our Services</li><li>Why Bright Pathways?</li><li>Blog</li><li>Contact Us</li>
</ul>

<div class="foot-heading abs" style="left:1000px;top:2612px">SOCIAL MEDIA</div>
<ul class="social abs">
  <li><span class="ring"></span>Circlebook</li>
  <li><span class="ring"></span>Chirper</li>
  <li><span class="ring"></span>Gather+</li>
  <li><span class="ring"></span>viewtube</li>
</ul>

<div class="foot-rule abs"></div>
<p class="copyright abs">Copyright © Bright Pathways 2017. All rights reserved.</p>

</body>
</html>
```